CD-/Plattencover für ein Harfen-Ensemble
Zielgruppe
Wir sind ein Ensemble von 3 Harfen und machen klassische Musik. Die Zielgruppe sind klassische Musikliebhaber von jung bis alt, die unkonventionelle Harfenmusik mögen. Das Programm hat spanischen Charakter.
Aufgabenstellung
Ein ansprechendes und schönes CD Cover, welches die Leidenschaft, Sehnsucht, Melancholie, Temperament der spanischen Musik um die Jahrhundertwende des 20. Jhdt. widerspiegelt.
Es sollte zumindest eine Harfe auf dem Cover zu erkennen sein, wenn auch nur stilistisch.
Fotos dürfen verwendet werden, falls auf dem Cover vorne, sollten die Menschen nur erahnt werden. Die Fotos dürfen gerne nach Belieben verwischt und bearbeitet werden, so dass man nur noch Züge oder Konturen erkennen kann.
Für die Rück-und Innenseite dürfte man die Personen auch erkennen.
Keine grellen Farben, eher warme Temperaturen.
Das Logo sollte irgendwo drauf sein, muss aber nicht auf die Vorderseite.
Der Name Velunessa sollte drauf. Unsere Namen Margit Ohlendorf, Liliane Brückner, Ottilie Kransfeld auf die Vorderseite. Velmorìa ist der Titel des Albums und sollte prominent sein.
Auf die Rückseite wirden die Stücke als Text darüber gelegt, bitte mit einbeziehen.
Denkbar wäre ein Design mit einem Schleier oder Spitzentuch (schwarz),oder einfach Spanische Spitze aks Element der in Verbindung mit der Harfe ist. Symbolisch für spanische Eleganz, Weiblichkeit, Tanz, Sehnsucht, Melancholie.....gedeckte Farben, Sepia, Gold, Bronze (Harfe).
Spanische aber schlicht-elegante Romantik.

```html
<!DOCTYPE html>
<html lang="de">
<head>
<meta charset="utf-8">
<title>Velmorìa – Velunessa drei Harfen</title>
<link rel="stylesheet" href="https://fonts.googleapis.com/css2?family=Barlow:wght@400;500&family=Barlow+Condensed:wght@400;600&family=Cormorant+Garamond:wght@400&display=swap">
<style>
  :root {
    --page: #ece7df;
    --ink-light: #f6f3ee;
    --veil-dark: #3b4033;
    --veil-mid: #6f7561;
    --veil-light: #c9ccbb;
    --harp-silver: #b7b2a5;
    --harp-bronze: #6e4a34;
    --harp-plum: #4a2f38;
    --photo-window: #b9c3b2;
    --photo-warm: #9a8372;
    --photo-dress: #1c1c20;
    --night: #0f1c27;
    --rule: #c9ced3;
  }
  * { box-sizing: border-box; margin: 0; padding: 0; }
  html, body { width: 817px; height: 1200px; overflow: hidden; }
  body { background: var(--page); position: relative; font-family: "Barlow", sans-serif; color: var(--ink-light); }

  .cover { position: absolute; left: 158px; width: 500px; height: 500px; overflow: hidden; }
  .cover--front { top: 48px; }
  .cover--back { top: 628px; background: var(--night); }

  /* Front */
  .veil-image { position: absolute; inset: 0;
    background:
      radial-gradient(ellipse at 85% 15%, var(--veil-light) 0%, transparent 55%),
      radial-gradient(ellipse at 10% 10%, #5d5f4d 0%, transparent 50%),
      linear-gradient(160deg, var(--veil-mid) 0%, var(--veil-dark) 55%, #2e3129 100%); }
  .harp-image { position: absolute; left: 0; right: 0; bottom: 0; height: 240px;
    background:
      linear-gradient(90deg, var(--harp-silver) 0%, #8d877b 14%, var(--harp-bronze) 26%, var(--harp-plum) 33%, #3a3a30 40%, var(--harp-bronze) 48%, #9a8f80 52%, var(--harp-plum) 58%, #3a3a30 64%, var(--harp-bronze) 72%, #8d877b 84%, var(--harp-silver) 100%);
    -webkit-mask-image: linear-gradient(to bottom, transparent 0%, #000 22%);
            mask-image: linear-gradient(to bottom, transparent 0%, #000 22%); }
  .front-ensemble { position: absolute; top: 118px; width: 100%; text-align: center;
    font-weight: 500; font-size: 15px; letter-spacing: 1.3px; }
  .front-members { position: absolute; top: 150px; width: 100%; display: flex; justify-content: center; gap: 16px;
    font-size: 11px; font-weight: 500; letter-spacing: 0.9px; text-transform: uppercase; }
  .front-title { position: absolute; top: 178px; width: 100%; text-align: center;
    font-family: "Cormorant Garamond", serif; font-size: 50px; letter-spacing: 11px; padding-left: 11px; }

  /* Back */
  .group-photo { position: absolute; left: 0; right: 0; top: 0; height: 330px;
    background:
      linear-gradient(to bottom, transparent 45%, var(--night) 100%),
      linear-gradient(90deg, var(--photo-window) 0%, var(--photo-warm) 14%, var(--photo-dress) 22%, #7b6a55 32%, var(--photo-warm) 45%, var(--photo-dress) 55%, var(--photo-warm) 66%, var(--photo-dress) 78%, var(--photo-window) 90%, var(--photo-window) 100%); }
  .back-logo { position: absolute; top: 118px; width: 100%; text-align: center;
    font-family: "Cormorant Garamond", serif; font-size: 38px; letter-spacing: 1px; }
  .back-members { position: absolute; top: 183px; width: 100%; display: flex; justify-content: center; gap: 12px;
    font-size: 8.5px; font-weight: 500; letter-spacing: 0.6px; text-transform: uppercase; }
  .back-title { position: absolute; top: 198px; width: 100%; text-align: center;
    font-family: "Cormorant Garamond", serif; font-size: 31px; letter-spacing: 6px; padding-left: 6px; }

  .tracklist { position: absolute; top: 250px; left: 20px; right: 20px; display: grid; grid-template-columns: 1fr 1fr; }
  .tracklist__column { padding-right: 10px; }
  .tracklist__column + .tracklist__column { border-left: 1px solid var(--rule); padding-left: 13px; padding-right: 0; margin-left: 0; }
  .track { display: grid; grid-template-columns: 37px 1fr auto; height: 47px; }
  .track__no { font-size: 11px; letter-spacing: 0.6px; }
  .track__composer { font-size: 11px; font-weight: 500; letter-spacing: 0.8px; text-transform: uppercase; }
  .track__years { font-size: 8px; letter-spacing: 0.6px; margin-left: 4px; font-weight: 400; }
  .track__work { grid-column: 2; font-family: "Barlow Condensed", sans-serif; font-size: 11.5px; letter-spacing: 0.4px; margin-top: 3px; }
  .track__time { grid-column: 3; grid-row: 2; font-family: "Barlow Condensed", sans-serif; font-size: 11px; margin-top: 3px; }

  .credits { position: absolute; top: 438px; width: 100%; text-align: center;
    font-family: "Barlow Condensed", sans-serif; font-size: 7.5px; line-height: 12px; letter-spacing: 0.2px; }
  .credits__print { font-weight: 600; }
</style>
</head>
<body>

<section class="cover cover--front">
  <div class="veil-image" role="img" aria-label="Schwarzer, fließender Schleierstoff in Oliv- und Grautönen"></div>
  <div class="harp-image" role="img" aria-label="Drei verzierte Harfensäulen mit Saiten in Silber, Bronze und Pflaume"></div>
  <p class="front-ensemble">VELUNESSA DREI HARFEN</p>
  <p class="front-members"><span>Margit Ohlendorf</span><span>Liliane Brückner</span><span>Ottilie Kransfeld</span></p>
  <h1 class="front-title">VELMORÌA</h1>
</section>

<section class="cover cover--back">
  <div class="group-photo" role="img" aria-label="Drei Harfenistinnen in schwarzen Spitzenkleidern vor einer Harfe in einem Raum mit hohen Fenstern"></div>
  <p class="back-logo">Velunessa</p>
  <p class="back-members"><span>Margit Ohlendorf</span><span>Liliane Brückner</span><span>Ottilie Kransfeld</span></p>
  <h2 class="back-title">VELMORÌA</h2>

  <div class="tracklist">
    <div class="tracklist__column">
      <div class="track"><span class="track__no">1-3</span><span class="track__composer">Komponist 1<span class="track__years">(1700-1750)</span></span><span></span><span class="track__work">Sonata A-Dur für drei Harfen</span><span class="track__time">12.03</span></div>
      <div class="track"><span class="track__no">4-6</span><span class="track__composer">Komponist 2<span class="track__years">(1700-1750)</span></span><span></span><span class="track__work">Sonata A-Dur für drei Harfen</span><span class="track__time">09.22</span></div>
      <div class="track"><span class="track__no">7-9</span><span class="track__composer">Komponist 3<span class="track__years">(1700-1750)</span></span><span></span><span class="track__work">Sonata A-Dur für drei Harfen</span><span class="track__time">11.51</span></div>
      <div class="track"><span class="track__no">10-12</span><span class="track__composer">Komponist 4<span class="track__years">(1700-1750)</span></span><span></span><span class="track__work">Sonata A-Dur für drei Harfen</span><span class="track__time">10.08</span></div>
    </div>
    <div class="tracklist__column">
      <div class="track"><span class="track__no">13-14</span><span class="track__composer">Komponist 5<span class="track__years">(1700-1750)</span></span><span></span><span class="track__work">Sonata A-Dur für drei Harfen</span><span class="track__time">07.26</span></div>
      <div class="track"><span class="track__no">15-17</span><span class="track__composer">Komponist 6<span class="track__years">(1700-1750)</span></span><span></span><span class="track__work">Sonata A-Dur für drei Harfen</span><span class="track__time">09.23</span></div>
      <div class="track"><span class="track__no">18-20</span><span class="track__composer">Komponist 7<span class="track__years">(1700-1750)</span></span><span></span><span class="track__work">Sonata A-Dur für drei Harfen</span><span class="track__time">13.03</span></div>
      <div class="track"><span class="track__no">21-23</span><span class="track__composer">Komponist 8<span class="track__years">(1700-1750)</span></span><span></span><span class="track__work">Sonata A-Dur für drei Harfen</span><span class="track__time">10.00</span></div>
    </div>
  </div>

  <div class="credits">
    <p>© 2018 Velunessa drei Harfen ♦ Aufnahme: Musterstadt, 01.10.2018</p>
    <p>Fotos: Velunessa / Lichtfeld (cover)</p>
    <p class="credits__print">Printed in Germany</p>
  </div>
</section>

</body>
</html>
```